Online trading school - Website design

We are building an online trading school (trading of shares, commodities, indices, currencies). The purpose is to teach online traders how to trade successfully. We need to design the homepage of the website and logo (bramwelloq.com will be the domain). The homepage will contain the following elements

- logo
- Sign in and Register links/buttons
- upper menu
- short introduction
- a couple of bullet points 'Why to join our school?'
- sign up form
- text
- bottom menu

Attached is a draft for the designer. The draft is just for an inspiration, the actual structure of the website can be different if the designer thinks so.

The designer is free to choose colors.

School

3 page

```html
<!DOCTYPE html>
<html lang="en">
<head>
<meta charset="utf-8">
<title>Bramwelloq – Online Trading School</title>
<link rel="stylesheet" href="https://fonts.googleapis.com/css2?family=Ubuntu:wght@300;400;500;700&display=swap">
<style>
  :root {
    --page-bg: #f4f4f5;
    --header-dark: #3b3c42;
    --header-mid: #5a5b62;
    --navy: #2b2a73;
    --green: #00c35f;
    --orange: #ff7f14;
    --nav-active: #3a8fe4;
    --text: #3c3c44;
    --muted: #6b6b73;
    --line: #cfcfd4;
    --white: #ffffff;
  }
  * { margin: 0; padding: 0; box-sizing: border-box; }
  html, body { width: 944px; height: 1200px; overflow: hidden; }
  body {
    position: relative;
    background: var(--page-bg);
    font-family: "Ubuntu", sans-serif;
    color: var(--text);
  }
  .header-backdrop {
    position: absolute; left: 0; top: 0; width: 944px; height: 370px;
    background: linear-gradient(120deg, var(--header-mid) 0%, var(--header-dark) 55%, #2e2f34 100%);
  }
  .brand {
    position: absolute; left: 150px; top: 54px;
    font-size: 36px; font-weight: 700; letter-spacing: 1px;
    color: var(--white);
  }
  .auth-btn {
    position: absolute; top: 46px; height: 36px;
    display: flex; align-items: center; justify-content: center;
    font-size: 11px; font-weight: 700; color: var(--white);
    text-transform: uppercase; letter-spacing: .3px;
  }
  .auth-btn.sign-in { left: 612px; width: 88px; background: var(--green); }
  .auth-btn.register { left: 706px; width: 88px; background: var(--orange); }
  .social { position: absolute; left: 701px; top: 96px; }
  .main-nav {
    position: absolute; top: 141px; left: 0; width: 944px;
    font-size: 14.5px; font-weight: 500; color: var(--white); text-transform: uppercase;
  }
  .main-nav a { position: absolute; color: inherit; text-decoration: none; white-space: nowrap; }
  .main-nav a.active { color: var(--nav-active); }
  .hero {
    position: absolute; left: 150px; top: 184px; width: 644px; height: 266px;
    background: linear-gradient(100deg, #dfe7ef 0%, #c9d3de 40%, #b7a79c 70%, #8e98a6 100%);
  }
  .hero-caption {
    position: absolute; left: 298px; top: 320px; width: 348px; height: 42px;
    background: rgba(70,70,72,.85); color: var(--white);
    font-size: 24px; font-weight: 300; display: flex; align-items: center; justify-content: center;
  }
  .slider-dots { position: absolute; left: 770px; top: 370px; }
  .content-card {
    position: absolute; left: 150px; top: 450px; width: 644px; height: 696px;
    background: var(--white); box-shadow: 0 2px 4px rgba(0,0,0,.18);
  }
  .section-title {
    position: absolute; color: var(--navy); font-size: 21px; font-weight: 700; text-transform: uppercase;
  }
  .why-title { left: 158px; top: 485px; }
  .why-list { position: absolute; left: 160px; top: 528px; list-style: none; font-size: 13.6px; font-weight: 300; color: var(--text); }
  .why-list li { height: 32px; position: relative; padding-left: 28px; }
  .why-list li::before { content: "›"; position: absolute; left: 0; top: -3px; font-size: 16px; }
  .signup-box {
    position: absolute; left: 423px; top: 466px; width: 365px; height: 304px;
    border: 1px solid #e6e6ea;
  }
  .signup-title { left: 438px; top: 485px; }
  .field {
    position: absolute; left: 438px; width: 334px; height: 38px;
    border: 1px solid var(--line); background: var(--white);
    display: flex; align-items: center; padding-left: 13px;
    font-size: 10.5px; color: var(--muted); font-weight: 300;
  }
  .field svg { margin-right: 12px; }
  .agree {
    position: absolute; left: 438px; top: 686px; display: flex; align-items: center;
    font-size: 10.5px; color: var(--text); font-weight: 300;
  }
  .agree .box { width: 16px; height: 16px; border: 1px solid var(--line); margin-right: 8px; }
  .submit {
    position: absolute; left: 438px; top: 717px; width: 334px; height: 36px;
    background: var(--green); color: var(--white); font-size: 13.5px; font-weight: 700;
    display: flex; align-items: center; justify-content: center;
  }
  .offer-title { left: 0; width: 944px; top: 828px; text-align: center; }
  .offer-text {
    position: absolute; left: 158px; width: 630px; text-align: center;
    font-size: 10.6px; line-height: 17.6px; font-weight: 300; color: var(--text);
  }
  .bottom-menu {
    position: absolute; left: 158px; top: 1080px; width: 630px; height: 51px;
    border: 1px solid var(--line); font-size: 10.5px; font-weight: 700; color: var(--text);
  }
  .bottom-menu span { position: absolute; top: 18px; transform: translateX(-50%); white-space: nowrap; }
  .copyright {
    position: absolute; top: 1167px; left: 0; width: 944px; text-align: center;
    font-size: 10.5px; font-weight: 300; color: var(--text);
  }
</style>
</head>
<body>
  <div class="header-backdrop" role="img" aria-label="Dimmed photo of a keyboard, banknotes and market charts"></div>

  <div class="brand">BRAMWELLOQ</div>

  <div class="auth-btn sign-in">Sign In</div>
  <div class="auth-btn register">Register</div>

  <svg class="social" width="94" height="28" viewBox="0 0 94 28" aria-label="Social links">
    <circle cx="14" cy="14" r="12.5" fill="none" stroke="#fff" stroke-width="1.3"/>
    <circle cx="46" cy="14" r="12.5" fill="none" stroke="#fff" stroke-width="1.3"/>
    <circle cx="79" cy="14" r="12.5" fill="none" stroke="#fff" stroke-width="1.3"/>
  </svg>

  <nav class="main-nav">
    <a class="active" style="left:173px">About Our School</a>
    <a style="left:348px">Risk Warning</a>
    <a style="left:486px">FAQ</a>
    <a style="left:546px">Trading Glossary</a>
    <a style="left:715px">Contact</a>
  </nav>

  <div class="hero" role="img" aria-label="Photo of a hand with a pen over a tablet showing trading charts"></div>
  <div class="hero-caption">We Are OnlineTrading School</div>
  <svg class="slider-dots" width="8" height="50" viewBox="0 0 8 50" aria-hidden="true">
    <circle cx="4" cy="4" r="3.5" fill="var(--green)"/>
    <circle cx="4" cy="17" r="3.5" fill="#fff"/>
    <circle cx="4" cy="31" r="3.5" fill="#fff"/>
    <circle cx="4" cy="45" r="3.5" fill="#fff"/>
  </svg>

  <div class="content-card"></div>

  <h2 class="section-title why-title">Why Join Us&nbsp; ?</h2>
  <ul class="why-list">
    <li>Best trading tipsever</li>
    <li>Secret tips from experts</li>
    <li>We teach you how to trade online</li>
    <li>Learn how to trade commodities</li>
    <li>Learn how to become a trader</li>
  </ul>

  <div class="signup-box"></div>
  <h2 class="section-title signup-title">Join Our School Now !</h2>
  <div class="field" style="top:526px">
    <svg width="9" height="10" viewBox="0 0 9 10"><circle cx="4.5" cy="2.6" r="2.4" fill="#777"/><path d="M0 10 Q0 5.5 4.5 5.5 Q9 5.5 9 10Z" fill="#777"/></svg>First Name</div>
  <div class="field" style="top:577px">
    <svg width="9" height="10" viewBox="0 0 9 10"><circle cx="4.5" cy="2.6" r="2.4" fill="#777"/><path d="M0 10 Q0 5.5 4.5 5.5 Q9 5.5 9 10Z" fill="#777"/></svg>Last Name</div>
  <div class="field" style="top:626px">
    <svg width="11" height="9" viewBox="0 0 11 9"><rect x=".6" y=".6" width="9.8" height="7.8" fill="none" stroke="#777" stroke-width="1.1"/><path d="M.6 .6 L5.5 5 L10.4 .6" fill="none" stroke="#777" stroke-width="1.1"/></svg>E-mail</div>
  <div class="agree"><span class="box"></span>Agree With Terms &amp; Conditions</div>
  <div class="submit">SUBMIT</div>

  <h2 class="section-title offer-title">What Do We Offer</h2>
  <p class="offer-text" style="top:889px">Lorem ipsum dolor sit amet, consectetur adipiscing elit, sed do eiusmod tempor incididunt ut labore et dolore magna aliqua. Ut enim ad minim veniam, quis nostrud exercitation ullamco laboris nisi ut aliquip ex ea commodo consequat. Duis aute irure dolor in reprehenderit in voluptate velit esse cillum dolore eu fugiat nulla pariatur. Excepteur sint occaecat cupidatat non proident, sunt in culpa qui officia deserunt mollit anim id est laborum.</p>
  <p class="offer-text" style="top:977px">Sed ut perspiciatis unde omnis iste natus error sit voluptatem accusantium doloremque laudantium, totam rem aperiam, eaque ipsa quae ab illo inventore veritatis et quasi architecto beatae vitae dicta sunt explicabo. Nemo enim ipsam voluptatem quia voluptas sit aspernatur aut odit aut fugit, sed quia consequuntur magni dolores eos qui ratione voluptatem sequi nesciunt.</p>

  <nav class="bottom-menu">
    <span style="left:208px">TERMS &amp; CONDITIONS</span>
    <span style="left:419px">PRIVACY PROTECTION</span>
  </nav>

  <footer class="copyright">© 2016 Company Name&nbsp; | All Rights Reserved</footer>
</body>
</html>
```